Brackenridge Window Company / Blind Sale postcard mailer

I need a Design for a two sided postcard, advertising products for our company. One side will mainly show blinds & shutters, and the "call out" will be "Blind Sale / $59.99 per window". Then a place underneath for details. The other side of the card can showcase our other products (shades, exterior, etc). I would like the overall look and feel of the card to resemble the website design and colors, etc, you see at www.larkmoorgoods.com and www.fennickhome.com. You can use any images from my Dropbox page here: https://www.filecrate-example.com/sh/7kq2wzv9tmrbelux/QQX4RRtuvPmWkad915JknDzLo?dl=0

Use images from the Quillbarrow folder in Dropbox.
Also, my website for reference is www.brackenridgewindows.com
Brackenridge Window Company

The printed card will be very plastic, heavy glossy. Heavier than most. I want the card to be as striking as possible, harder for customer to throw away. Trying to avoid lots of clutter on the card. Custom Template attached.

Target Market(s)

Card will be targeted mainly to new homeowners, especially new construction homes

Industry/Entity Type

It Company

Font styles to use
Serif
Sans Serif

Requirements
Must have
• Clean, uncluttered look. Best looking images. Logo somewhere on card. Open to changing the color of logo (i.e., if whites and greys are the main color, could do a white and grey version of logo..)

```html
<!DOCTYPE html>
<html lang="en">
<head>
<meta charset="utf-8">
<title>Brackenridge Window Company – Blind Sale Postcard</title>
<link href="https://fonts.googleapis.com/css2?family=Raleway:wght@400&family=Roboto+Condensed:wght@400;700&family=Montserrat:wght@400&display=swap" rel="stylesheet">
<style>
  :root{
    --page:#e9e7e4;
    --card:#ffffff;
    --footer:#231f20;
    --price-band:#7b624b;
    --white:#ffffff;
    --box-line:#c9c9c9;
    --shadow:rgba(0,0,0,.28);
    --photo-dining:linear-gradient(135deg,#3b2a1f 0%,#7a6347 45%,#cdbb9c 70%,#5a4634 100%);
    --photo-exterior:linear-gradient(160deg,#d9dde0 0%,#8e9397 55%,#45403a 100%);
    --photo-porch:linear-gradient(150deg,#f1ede6 0%,#8a5a2e 50%,#5c3b22 100%);
    --photo-white-room:linear-gradient(140deg,#f3f0ea 0%,#b9ada0 55%,#4a3b31 100%);
    --photo-wood-room:linear-gradient(140deg,#8c4f2a 0%,#b06a3d 50%,#4a2a18 100%);
    --photo-blinds:linear-gradient(100deg,#e8e2d7 0%,#9a5a30 40%,#5b3420 70%,#a2643a 100%);
    --photo-office:linear-gradient(120deg,#6e3b1e 0%,#b37245 45%,#c9a37c 70%,#3d2416 100%);
    --photo-lounge:linear-gradient(120deg,#5a4433 0%,#c27a3e 45%,#d9d2c6 100%);
    --photo-living:linear-gradient(110deg,#dad6c8 0%,#7f7a3c 40%,#f1efe9 70%,#c9c2b1 100%);
  }
  *{box-sizing:border-box;margin:0;padding:0}
  html,body{width:1200px;height:1115px;overflow:hidden;background:var(--page)}
  .canvas{position:relative;width:1200px;height:1115px}

  .postcard{position:absolute;width:987px;height:485px;background:var(--card);box-shadow:4px 6px 12px var(--shadow);overflow:hidden}
  .postcard--front{left:56px;top:45px}
  .postcard--back{left:156px;top:591px}

  .photo{position:absolute}
  .footer{position:absolute;left:0;right:0;bottom:0;height:42px;background:var(--footer);
    display:flex;align-items:center;justify-content:center;
    font-family:'Montserrat',sans-serif;font-size:12px;letter-spacing:4px;color:var(--white)}

  .brand-title{position:absolute;font-family:'Raleway',sans-serif;font-weight:400;color:var(--white);
    text-transform:uppercase;text-align:center;line-height:1.5;text-shadow:0 1px 3px rgba(0,0,0,.35)}
  .postcard--front .brand-title{left:18px;top:26px;font-size:33px}
  .postcard--back .brand-title{left:14px;top:26px;font-size:26px;line-height:1.6}

  .price-band{position:absolute;left:0;top:193px;width:569px;height:95px;background:var(--price-band);
    display:flex;align-items:center;color:var(--white);font-family:'Roboto Condensed',sans-serif}
  .price-band__tag{writing-mode:vertical-rl;transform:rotate(180deg);font-size:12px;letter-spacing:.5px;margin-left:24px;margin-right:10px}
  .price-band__amount{font-weight:700;font-size:70px;line-height:1}
  .price-band__unit{font-size:44px;margin-left:20px;margin-top:14px;line-height:1}

  .stamp-box{position:absolute;left:889px;top:32px;width:69px;height:43px;border:1px solid var(--box-line)}
  .address-box{position:absolute;left:662px;width:330px;border:1px solid var(--box-line);border-right:none}
  .address-box--top{top:85px;height:107px}
  .address-box--bottom{top:278px;height:134px}
</style>
</head>
<body>
<main class="canvas">

  <section class="postcard postcard--front">
    <div class="photo" role="img" aria-label="Dining room with plantation shutters in a bay window" style="left:0;top:0;width:524px;height:434px;background:var(--photo-dining)"></div>
    <div class="photo" role="img" aria-label="Exterior Bahama shutters over a porch" style="left:531px;top:0;width:221px;height:161px;background:var(--photo-exterior)"></div>
    <div class="photo" role="img" aria-label="Exterior roller shade on a porch" style="left:759px;top:0;width:228px;height:161px;background:var(--photo-porch)"></div>
    <div class="photo" role="img" aria-label="Bright white room with shutters and vaulted ceiling" style="left:531px;top:170px;width:221px;height:163px;background:var(--photo-white-room)"></div>
    <div class="photo" role="img" aria-label="Wood paneled study with stained shutters" style="left:759px;top:170px;width:228px;height:163px;background:var(--photo-wood-room)"></div>
    <div class="photo" role="img" aria-label="Living room with wood blinds and sofa" style="left:531px;top:342px;width:456px;height:92px;background:var(--photo-blinds)"></div>
    <h1 class="brand-title">Brackenridge<br>Window<br>Company</h1>
    <footer class="footer">WWW.BRACKENRIDGEWINDOWS.COM</footer>
  </section>

  <section class="postcard postcard--back">
    <div class="photo" role="img" aria-label="Home office with wood shutters and desk" style="left:0;top:0;width:569px;height:182px;background:var(--photo-office)"></div>
    <h2 class="brand-title">Brackenridge<br>Window<br>Company</h2>
    <div class="price-band">
      <span class="price-band__tag">BLIND SALE</span>
      <span class="price-band__amount">$59.99</span>
      <span class="price-band__unit">PER WINDOW</span>
    </div>
    <div class="photo" role="img" aria-label="Lounge with wood blinds and armchair" style="left:0;top:294px;width:283px;height:140px;background:var(--photo-lounge)"></div>
    <div class="photo" role="img" aria-label="Living room with light shades and green drapes" style="left:291px;top:294px;width:278px;height:140px;background:var(--photo-living)"></div>
    <div class="stamp-box"></div>
    <div class="address-box address-box--top"></div>
    <div class="address-box address-box--bottom"></div>
    <footer class="footer">WWW.BRACKENRIDGEWINDOWS.COM</footer>
  </section>

</main>
</body>
</html>
```